Dune Business Card Design Project

We have an existing business card. We are looking to creat a new card for the store. I have attached a my own business so you have a refference of what the current card looks like.

Phone: 1300 574 213
email: merrow@dunepanes.com.au
website: www.dunepanes.com.au
Address: (Inside Merrow Rug Hall) 418 Tolvey Rd, Pelbrook VIC 3158
Updates

This is a new business card for our store.

Industry/Entity Type

Business

Requirements
Must have
• Must look similar to the existing card

```html
<!DOCTYPE html>
<html lang="en">
<head>
<meta charset="UTF-8">
<title>Dune Shutters and Blinds – Business Card</title>
<link rel="stylesheet" href="https://fonts.googleapis.com/css2?family=Arimo:wght@400&display=swap">
<style>
  :root {
    --card-dark: #121517;
    --card-light: #ffffff;
    --brand-grey: #7a7a7a;
    --tagline-light: #c4c4c4;
    --tagline-dark: #a9a9a9;
    --accent-red: #e3231c;
    --text-white: #ffffff;
    --text-black: #111111;
    --rule-grey: #8c8c8c;
  }
  * { margin: 0; padding: 0; box-sizing: border-box; }
  html, body {
    width: 957px;
    height: 1200px;
    overflow: hidden;
    background: var(--card-light);
    font-family: "Arimo", Arial, sans-serif;
  }
  .sheet { position: relative; width: 957px; height: 1200px; }

  .card-front {
    position: absolute; left: 0; top: 0;
    width: 957px; height: 603px;
    background: var(--card-dark);
  }
  .card-back {
    position: absolute; left: 0; top: 603px;
    width: 957px; height: 597px;
    background: var(--card-light);
  }

  .wordmark {
    position: absolute;
    font-weight: 400;
    font-size: 150px;
    line-height: 1;
    letter-spacing: 1px;
    white-space: nowrap;
  }
  .card-front .wordmark { left: 30px; top: 60px; color: var(--brand-grey); }
  .card-back .wordmark { left: 166px; top: 166px; color: var(--text-black); }

  .tagline {
    position: absolute;
    font-size: 37px;
    line-height: 1;
    white-space: nowrap;
  }
  .card-front .tagline { left: 40px; top: 216px; color: var(--tagline-light); }
  .card-back .tagline { left: 175px; top: 918px; top: 315px; color: var(--tagline-dark); }

  .holder { position: absolute; left: 659px; top: 112px; }
  .holder-name {
    font-size: 40px;
    color: var(--accent-red);
    line-height: 1;
    white-space: nowrap;
  }
  .holder-role {
    font-size: 21px;
    color: var(--text-white);
    line-height: 1;
    margin-top: 2px;
  }

  .contact-list {
    position: absolute; left: 30px; top: 362px;
    list-style: none;
  }
  .contact-item {
    display: flex; align-items: center;
    height: 26.6px;
    font-size: 16.5px;
    color: var(--text-white);
    white-space: nowrap;
  }
  .contact-icon { width: 22px; height: 14px; margin-right: 8px; flex: none; }

  .rule { position: absolute; border-radius: 3px 0 0 3px; }
  .card-front .rule {
    left: 766px; top: 464px; width: 191px; height: 6px;
    background: linear-gradient(to right, rgba(140,140,140,0), var(--rule-grey));
  }
  .card-back .rule {
    left: 550px; top: 456px; width: 407px; height: 8px;
    background: linear-gradient(to right, rgba(140,140,140,0), #6e6e6e);
  }

  .site-line {
    position: absolute; left: 646px; top: 432px;
    font-size: 22px;
    line-height: 1;
    color: var(--text-black);
    white-space: nowrap;
  }
</style>
</head>
<body>
<div class="sheet">

  <section class="card-front">
    <div class="wordmark">Dune</div>
    <div class="tagline">Shutters and Blinds</div>

    <div class="holder">
      <div class="holder-name">Dylan Varga</div>
      <div class="holder-role">Director</div>
    </div>

    <ul class="contact-list">
      <li class="contact-item">
        <svg class="contact-icon" viewBox="0 0 22 14" aria-hidden="true"><g fill="#fff"><circle cx="11" cy="4" r="3"/><circle cx="5" cy="10" r="3"/><circle cx="17" cy="10" r="3"/></g></svg>
        Mobile : 0412 305 961
      </li>
      <li class="contact-item">
        <svg class="contact-icon" viewBox="0 0 22 14" aria-hidden="true"><g fill="#fff"><circle cx="11" cy="4" r="3"/><circle cx="5" cy="10" r="3"/><circle cx="17" cy="10" r="3"/></g></svg>
        Phone : 1300 574 213
      </li>
      <li class="contact-item">
        <svg class="contact-icon" viewBox="0 0 22 14" aria-hidden="true"><g fill="#fff"><circle cx="11" cy="4" r="3"/><circle cx="5" cy="10" r="3"/><circle cx="17" cy="10" r="3"/></g></svg>
        Email : merrow@dunepanes.com.au
      </li>
      <li class="contact-item">
        <svg class="contact-icon" viewBox="0 0 22 14" aria-hidden="true"><g fill="#fff"><circle cx="11" cy="4" r="3"/><circle cx="5" cy="10" r="3"/><circle cx="17" cy="10" r="3"/></g></svg>
        Address : (Inside Merrow Rug Hall) 418 Tolvey Rd, Pelbrook VIC 3158
      </li>
      <li class="contact-item">
        <svg class="contact-icon" viewBox="0 0 22 14" aria-hidden="true"><g fill="#fff"><circle cx="11" cy="4" r="3"/><circle cx="5" cy="10" r="3"/><circle cx="17" cy="10" r="3"/></g></svg>
        Website : www.dunepanes.com.au
      </li>
    </ul>

    <div class="rule"></div>
  </section>

  <section class="card-back">
    <div class="wordmark">Dune</div>
    <div class="tagline">Shutters and Blinds</div>
    <div class="site-line">www.dunepanes.com.au</div>
    <div class="rule"></div>
  </section>

</div>
</body>
</html>
```